Spice Mix Label Bottle Branding - Health and Weight Loss Mixes

The company is called ZestRow Spice Mix's. We've created 5 spice mixes using ingredients that promote health and weight loss. We already have a logo but now we need labels for our bottles. We would like to see designs that have the feel of health supplements (see attached examples)

We would like a different colour featured with each of our flavours.

Our flavours are:
-Golden Chai (Yellow)
-Mild Curry (Orange)
-Coffee Rub (brown)
-Garlic Oregano (Green)
-Taco (Blue)

Thank you!

Target Market(s)

Ages 22-35. Men and Female. Trendy, Hipster.

Industry/Entity Type

Food Production

Font styles to use
Sans Serif

Colors
f37122
0655a3
0692cd
9bcb3c
fbee3f

Requirements
Must have
• A different featured colour for each flavour.
• The ZestRow Spices Logo (attached)
• The slogan: "Weight Loss Ingredients"
• -Golden Chai (Yellow)
• -Mild Curry (Orange)
• -Coffee Rub (brown)
• -Garlic Oregano (Green)
• -Taco (Blue)
• Text Files attached.
Nice to have
• A black label with a featured colour for each of the spice mice flavours.
• 'No Salt added'

```html
<!DOCTYPE html>
<html lang="en">
<head>
<meta charset="utf-8">
<title>ZestRow Spices – Flavour Labels</title>
<link rel="stylesheet" href="https://fonts.googleapis.com/css2?family=Oswald:wght@500;600&display=swap">
<style>
  :root {
    --label-black: #000000;
    --page-white: #ffffff;
    --ink-white: #ffffff;
    --golden-chai: #d99a2b;
    --mild-curry: #f04e23;
    --garlic-oregano: #9bbb3c;
    --coffee-rub: #9a6430;
    --taco: #2f67a6;
  }
  html, body {
    margin: 0;
    padding: 0;
    width: 875px;
    height: 1200px;
    overflow: hidden;
    background: var(--page-white);
  }
  .label-sheet {
    position: absolute;
    top: 14px;
    left: 10px;
    width: 854px;
    display: flex;
    flex-direction: column;
    gap: 1px;
  }
  .flavour-label {
    display: block;
    width: 854px;
    height: 233px;
    background: var(--label-black);
    overflow: hidden;
  }
  .flavour-label svg { display: block; }
  .flavour-name {
    font-family: "Oswald", sans-serif;
    font-weight: 500;
    font-size: 17px;
    letter-spacing: 2px;
    fill: var(--ink-white);
  }
  .brand-name {
    font-family: "Oswald", sans-serif;
    font-weight: 600;
    fill: var(--ink-white);
  }
  .brand-word { font-size: 54px; }
  .brand-sub { font-size: 11px; letter-spacing: 7px; }
  .slogan {
    font-family: "Oswald", sans-serif;
    font-weight: 600;
    font-size: 8px;
    letter-spacing: 0.2px;
    fill: var(--ink-white);
  }
  .no-salt {
    font-family: "Oswald", sans-serif;
    font-weight: 500;
    font-size: 11px;
    letter-spacing: 1.5px;
    fill: var(--ink-white);
  }
  .golden-chai { --accent: var(--golden-chai); }
  .mild-curry { --accent: var(--mild-curry); }
  .garlic-oregano { --accent: var(--garlic-oregano); }
  .coffee-rub { --accent: var(--coffee-rub); }
  .taco { --accent: var(--taco); }
  .sunburst { fill: var(--accent); }
  .badge-disc { fill: var(--label-black); }
  .badge-ring { fill: none; stroke: var(--accent); stroke-width: 2; }
  .accent-rule { stroke: var(--accent); stroke-width: 1.2; }
  .accent-dot { fill: var(--accent); }
</style>
</head>
<body>
<main class="label-sheet">

  <section class="flavour-label golden-chai">
    <svg width="854" height="233" viewBox="0 0 854 233">
      <defs>
        <path id="top-arc-chai" d="M -72 0 A 72 72 0 0 1 72 0"/>
        <path id="bottom-arc-chai" d="M -84 0 A 84 84 0 0 0 84 0"/>
      </defs>
      <g transform="translate(427 116.5)">
        <circle class="sunburst" r="156" role="img" aria-label="Radiating sunburst of spice rays in golden yellow"/>
        <circle class="badge-disc" r="103"/>
        <circle class="badge-ring" r="95"/>
        <text class="flavour-name" text-anchor="middle"><textPath href="#top-arc-chai" startOffset="50%">GOLDEN CHAI</textPath></text>
        <line class="accent-rule" x1="-74" y1="-40" x2="-14" y2="-40"/>
        <line class="accent-rule" x1="14" y1="-40" x2="74" y2="-40"/>
        <text class="brand-name" text-anchor="middle"><tspan class="brand-word" x="0" y="20">ZestRow</tspan><tspan class="brand-sub" x="3" y="38">SPICES</tspan></text>
        <text class="slogan" x="0" y="53" text-anchor="middle">WEIGHT LOSS INGREDIENTS</text>
        <line class="accent-rule" x1="-52" y1="58" x2="52" y2="58"/>
        <circle class="accent-dot" cx="-5" cy="61" r="1.3"/><circle class="accent-dot" cx="0" cy="61" r="1.3"/><circle class="accent-dot" cx="5" cy="61" r="1.3"/>
        <text class="no-salt" text-anchor="middle"><textPath href="#bottom-arc-chai" startOffset="50%">NO SALT ADDED</textPath></text>
      </g>
    </svg>
  </section>

  <section class="flavour-label mild-curry">
    <svg width="854" height="233" viewBox="0 0 854 233">
      <defs>
        <path id="top-arc-curry" d="M -72 0 A 72 72 0 0 1 72 0"/>
        <path id="bottom-arc-curry" d="M -84 0 A 84 84 0 0 0 84 0"/>
      </defs>
      <g transform="translate(427 116.5)">
        <circle class="sunburst" r="156" role="img" aria-label="Radiating sunburst of spice rays in orange"/>
        <circle class="badge-disc" r="103"/>
        <circle class="badge-ring" r="95"/>
        <text class="flavour-name" text-anchor="middle"><textPath href="#top-arc-curry" startOffset="50%">MILD CURRY</textPath></text>
        <line class="accent-rule" x1="-74" y1="-40" x2="-14" y2="-40"/>
        <line class="accent-rule" x1="14" y1="-40" x2="74" y2="-40"/>
        <text class="brand-name" text-anchor="middle"><tspan class="brand-word" x="0" y="20">ZestRow</tspan><tspan class="brand-sub" x="3" y="38">SPICES</tspan></text>
        <text class="slogan" x="0" y="53" text-anchor="middle">WEIGHT LOSS INGREDIENTS</text>
        <line class="accent-rule" x1="-52" y1="58" x2="52" y2="58"/>
        <circle class="accent-dot" cx="-5" cy="61" r="1.3"/><circle class="accent-dot" cx="0" cy="61" r="1.3"/><circle class="accent-dot" cx="5" cy="61" r="1.3"/>
        <text class="no-salt" text-anchor="middle"><textPath href="#bottom-arc-curry" startOffset="50%">NO SALT ADDED</textPath></text>
      </g>
    </svg>
  </section>

  <section class="flavour-label garlic-oregano">
    <svg width="854" height="233" viewBox="0 0 854 233">
      <defs>
        <path id="top-arc-garlic" d="M -72 0 A 72 72 0 0 1 72 0"/>
        <path id="bottom-arc-garlic" d="M -84 0 A 84 84 0 0 0 84 0"/>
      </defs>
      <g transform="translate(427 116.5)">
        <circle class="sunburst" r="156" role="img" aria-label="Radiating sunburst of spice rays in green"/>
        <circle class="badge-disc" r="103"/>
        <circle class="badge-ring" r="95"/>
        <text class="flavour-name" text-anchor="middle"><textPath href="#top-arc-garlic" startOffset="50%">GARLIC OREGANO</textPath></text>
        <line class="accent-rule" x1="-74" y1="-40" x2="-14" y2="-40"/>
        <line class="accent-rule" x1="14" y1="-40" x2="74" y2="-40"/>
        <text class="brand-name" text-anchor="middle"><tspan class="brand-word" x="0" y="20">ZestRow</tspan><tspan class="brand-sub" x="3" y="38">SPICES</tspan></text>
        <text class="slogan" x="0" y="53" text-anchor="middle">WEIGHT LOSS INGREDIENTS</text>
        <line class="accent-rule" x1="-52" y1="58" x2="52" y2="58"/>
        <circle class="accent-dot" cx="-5" cy="61" r="1.3"/><circle class="accent-dot" cx="0" cy="61" r="1.3"/><circle class="accent-dot" cx="5" cy="61" r="1.3"/>
        <text class="no-salt" text-anchor="middle"><textPath href="#bottom-arc-garlic" startOffset="50%">NO SALT ADDED</textPath></text>
      </g>
    </svg>
  </section>

  <section class="flavour-label coffee-rub">
    <svg width="854" height="233" viewBox="0 0 854 233">
      <defs>
        <path id="top-arc-coffee" d="M -72 0 A 72 72 0 0 1 72 0"/>
        <path id="bottom-arc-coffee" d="M -84 0 A 84 84 0 0 0 84 0"/>
      </defs>
      <g transform="translate(427 116.5)">
        <circle class="sunburst" r="156" role="img" aria-label="Radiating sunburst of spice rays in coffee brown"/>
        <circle class="badge-disc" r="103"/>
        <circle class="badge-ring" r="95"/>
        <text class="flavour-name" text-anchor="middle"><textPath href="#top-arc-coffee" startOffset="50%">COFFEE RUB</textPath></text>
        <line class="accent-rule" x1="-74" y1="-40" x2="-14" y2="-40"/>
        <line class="accent-rule" x1="14" y1="-40" x2="74" y2="-40"/>
        <text class="brand-name" text-anchor="middle"><tspan class="brand-word" x="0" y="20">ZestRow</tspan><tspan class="brand-sub" x="3" y="38">SPICES</tspan></text>
        <text class="slogan" x="0" y="53" text-anchor="middle">WEIGHT LOSS INGREDIENTS</text>
        <line class="accent-rule" x1="-52" y1="58" x2="52" y2="58"/>
        <circle class="accent-dot" cx="-5" cy="61" r="1.3"/><circle class="accent-dot" cx="0" cy="61" r="1.3"/><circle class="accent-dot" cx="5" cy="61" r="1.3"/>
        <text class="no-salt" text-anchor="middle"><textPath href="#bottom-arc-coffee" startOffset="50%">NO SALT ADDED</textPath></text>
      </g>
    </svg>
  </section>

  <section class="flavour-label taco">
    <svg width="854" height="233" viewBox="0 0 854 233">
      <defs>
        <path id="top-arc-taco" d="M -72 0 A 72 72 0 0 1 72 0"/>
        <path id="bottom-arc-taco" d="M -84 0 A 84 84 0 0 0 84 0"/>
      </defs>
      <g transform="translate(427 116.5)">
        <circle class="sunburst" r="156" role="img" aria-label="Radiating sunburst of spice rays in blue"/>
        <circle class="badge-disc" r="103"/>
        <circle class="badge-ring" r="95"/>
        <text class="flavour-name" text-anchor="middle"><textPath href="#top-arc-taco" startOffset="50%">TACO</textPath></text>
        <line class="accent-rule" x1="-74" y1="-40" x2="-14" y2="-40"/>
        <line class="accent-rule" x1="14" y1="-40" x2="74" y2="-40"/>
        <text class="brand-name" text-anchor="middle"><tspan class="brand-word" x="0" y="20">ZestRow</tspan><tspan class="brand-sub" x="3" y="38">SPICES</tspan></text>
        <text class="slogan" x="0" y="53" text-anchor="middle">WEIGHT LOSS INGREDIENTS</text>
        <line class="accent-rule" x1="-52" y1="58" x2="52" y2="58"/>
        <circle class="accent-dot" cx="-5" cy="61" r="1.3"/><circle class="accent-dot" cx="0" cy="61" r="1.3"/><circle class="accent-dot" cx="5" cy="61" r="1.3"/>
        <text class="no-salt" text-anchor="middle"><textPath href="#bottom-arc-taco" startOffset="50%">NO SALT ADDED</textPath></text>
      </g>
    </svg>
  </section>

</main>
</body>
</html>
```